Mt Brindlewood Hotel

We need a business card with old world charm.
The design will need to promote dining and accommodation for local residents as a place to relax and for vacationing or week-end visitors seeking an experience of country hospitality.
The hotel was originally opened in 1909.

Target Market(s)

Adults and Families searching for dining and accommodation.

Industry/Entity Type

Business

Requirements
Nice to have
• Sketch or line drawing of Hotel

```html
<!DOCTYPE html>
<html lang="en">
<head>
<meta charset="utf-8">
<title>Mt Brindlewood Hotel – Business Card</title>
<link href="https://fonts.googleapis.com/css2?family=Sorts+Mill+Goudy:ital@0;1&display=swap" rel="stylesheet">
<style>
  :root {
    --wood-light: #efd3a6;
    --wood-mid: #e6c390;
    --wood-dark: #dcb47e;
    --ink: #7b5532;
    --ink-soft: #8c6844;
    --photo-tone: #b08a5c;
    --photo-shade: #8d6a44;
    --seam: rgba(255, 240, 215, 0.7);
  }
  * { margin: 0; padding: 0; box-sizing: border-box; }
  html, body {
    width: 1200px; height: 347px; overflow: hidden;
    background: var(--wood-mid);
  }
  .card-sheet {
    position: relative;
    width: 1200px; height: 347px;
    display: flex;
    font-family: "Sorts Mill Goudy", "Goudy Old Style", Georgia, serif;
    color: var(--ink);
  }
  .card-face {
    position: relative;
    height: 100%;
    background:
      repeating-linear-gradient(92deg, rgba(255,255,255,0.05) 0 3px, rgba(120,80,30,0.04) 3px 7px),
      linear-gradient(180deg, var(--wood-light), var(--wood-mid) 55%, var(--wood-dark));
  }
  .card-front { width: 603px; }
  .card-back { width: 597px; border-left: 3px solid var(--seam); }

  .front-title {
    position: absolute; left: 0; width: 603px; top: 18px;
    text-align: center;
    font-size: 50px; line-height: 1;
    color: var(--ink-soft);
    letter-spacing: 0.5px;
  }
  .hotel-sketch {
    position: absolute; left: 112px; top: 95px;
    width: 380px; height: 198px;
    border: 3px solid var(--ink-soft);
    background: linear-gradient(180deg, var(--photo-tone), var(--photo-shade));
  }
  .front-subtitle {
    position: absolute; left: 0; width: 603px; top: 296px;
    text-align: center;
    font-size: 36px; line-height: 1;
    color: var(--ink-soft);
  }

  .back-lines {
    position: absolute; inset: 0;
    display: flex; flex-direction: column; align-items: center;
    text-align: center;
  }
  .back-name { position: absolute; top: 36px; font-size: 26px; font-weight: 400; }
  .back-tagline { position: absolute; font-style: italic; font-size: 31px; }
  .tagline-dining { top: 103px; }
  .tagline-hospitality { top: 183px; }
  .back-since { position: absolute; top: 266px; font-size: 27px; }
</style>
</head>
<body>
  <div class="card-sheet">
    <section class="card-face card-front">
      <h1 class="front-title">Mt Brindlewood</h1>
      <div class="hotel-sketch" role="img" aria-label="Sepia sketch of the two-storey country hotel building with verandah"></div>
      <p class="front-subtitle">Hotel</p>
    </section>
    <section class="card-face card-back">
      <div class="back-lines">
        <h2 class="back-name">Mt Brindlewood Hotel</h2>
        <p class="back-tagline tagline-dining">Great dining &amp; accommodation</p>
        <p class="back-tagline tagline-hospitality">Real country hospitality</p>
        <p class="back-since">Since 1909.</p>
      </div>
    </section>
  </div>
</body>
</html>
```